International Vacuum Business Needs a Business Card

We need a business card design for a new company based in Toronto called "Plumora-Sweep". We will be selling and installing a proprietary central vacuum system that is one of a kind to the condominium market mainly through various large builders throughout the country as well as a second distribution chain at a retail level. Our product has a very unique retractable hose system that allows the hose to be stored away within the walls of a space all by the push of a button. "No more hoses laying around the house" We would like to see the design use the colours Red, Black, Grey and possibly white. The design should communicate the following terms " sleek, discreet, convenient, sophisticated, modern"
Updates

Project Deadline Extended
Reason: Hello All, I have not been able to provide very much feedback as I have been unavailable this week so we will be extending the deadline for another 3 days. Thanks,

Project Deadline Extended
Reason: Hello All, The revision and feedback process has been slow so I have no choice but to extend once again. We are still looking for that one great design. Thank you

Project Deadline Extended
Reason: Guys the feedback and changes on some of the designs are taking really long from some of you so I have no choice but to continue extending the deadline forward.

Target Market(s)

Our target market is male/female aged 25-65, more so focussing on 25-50.

Industry/Entity Type

Retail

Requirements
Must have
• Phone #
Fax #
Mobile #
Toll Free #
Web site address "www.plumorasweep.ca"

```html
<!DOCTYPE html>
<html lang="en">
<head>
<meta charset="utf-8">
<title>Plumora-Sweep Business Card</title>
<link rel="stylesheet" href="https://fonts.googleapis.com/css2?family=Quicksand:wght@500&family=Source+Sans+3:wght@400&display=swap">
<style>
  :root {
    --card-black: #050505;
    --brand-red: #b3141d;
    --paper: #ffffff;
    --ink-light: #ffffff;
  }
  html, body {
    margin: 0;
    padding: 0;
    width: 1045px;
    height: 1200px;
    overflow: hidden;
    background: var(--paper);
  }
  .sheet {
    position: relative;
    width: 1045px;
    height: 1200px;
  }
  .card {
    position: absolute;
    background: var(--card-black);
    overflow: hidden;
    color: var(--ink-light);
    font-family: "Source Sans 3", "Myriad Pro", Arial, sans-serif;
  }
  .card--front { left: 71px; top: 41px; width: 917px; height: 526px; }
  .card--back  { left: 61px; top: 657px; width: 914px; height: 522px; }

  .accent-bar { position: absolute; background: var(--brand-red); }
  .card--front .accent-bar { left: 43px; top: 0; width: 55px; height: 143px; }
  .card--back .accent-bar { left: 767px; top: 0; width: 55px; height: 100%; }

  .brand-name {
    font-family: "Quicksand", "Century Gothic", sans-serif;
    font-weight: 500;
    color: var(--ink-light);
    white-space: nowrap;
    letter-spacing: 1px;
  }
  .brand-square { display: inline-block; background: var(--brand-red); }

  .front-brand {
    position: absolute;
    left: 439px; top: 41px;
    display: flex; align-items: center; gap: 16px;
  }
  .front-brand .brand-square { width: 52px; height: 52px; }
  .front-brand .brand-name { font-size: 42px; }
  .front-url {
    position: absolute;
    left: 513px; top: 104px;
    font-size: 31px;
  }

  .holder-name {
    position: absolute; left: 45px; top: 154px;
    margin: 0; font-size: 44px; font-weight: 400; letter-spacing: 0.5px;
  }
  .holder-title {
    position: absolute; left: 47px; top: 204px;
    margin: 0; font-size: 28px;
  }

  .contact-list { position: absolute; left: 43px; top: 259px; margin: 0; padding: 0; list-style: none; }
  .contact-item { display: flex; align-items: center; height: 48px; margin-bottom: 20px; }
  .contact-label {
    background: var(--brand-red);
    font-size: 22px;
    height: 48px; line-height: 48px;
    min-width: 55px; padding: 0 4px; box-sizing: border-box;
    text-align: center;
  }
  .contact-value { font-size: 31px; margin-left: 20px; }

  .front-emblem {
    position: absolute; left: 645px; top: 261px;
    width: 235px; height: 235px;
  }

  .back-emblem {
    position: absolute; left: 290px; top: 92px;
    width: 175px; height: 165px;
  }
  .back-brand {
    position: absolute; left: 0; width: 754px; top: 270px;
    text-align: center; font-size: 64px;
  }
  .back-url {
    position: absolute; left: 0; width: 754px; top: 374px;
    text-align: center; font-size: 44px;
  }
</style>
</head>
<body>
<main class="sheet">
  <section class="card card--front" aria-label="Business card front">
    <div class="accent-bar"></div>
    <div class="front-brand">
      <span class="brand-square"></span>
      <span class="brand-name">Plumora-Sweep</span>
    </div>
    <div class="front-url">www.plumorasweep.ca</div>

    <h1 class="holder-name">DANIEL MARSH</h1>
    <p class="holder-title">President</p>

    <ul class="contact-list">
      <li class="contact-item"><span class="contact-label">Tel</span><span class="contact-value">(416) 555-0142</span></li>
      <li class="contact-item"><span class="contact-label">Mob</span><span class="contact-value">(416) 555-0143</span></li>
      <li class="contact-item"><span class="contact-label">Fax</span><span class="contact-value">(416) 555-0144</span></li>
      <li class="contact-item"><span class="contact-label">Tel</span><span class="contact-value">1-800-555-0199</span></li>
    </ul>

    <svg class="front-emblem" viewBox="0 0 235 235" aria-hidden="true">
      <rect x="0" y="0" width="235" height="235" fill="var(--brand-red)"/>
    </svg>
  </section>

  <section class="card card--back" aria-label="Business card back">
    <div class="accent-bar"></div>
    <svg class="back-emblem" viewBox="0 0 175 165" aria-hidden="true">
      <rect x="5" y="0" width="165" height="165" fill="var(--brand-red)"/>
    </svg>
    <div class="brand-name back-brand">Plumora-Sweep</div>
    <div class="back-url">www.plumorasweep.ca</div>
  </section>
</main>
</body>
</html>
```